modern real estate design
business card/letterhead/envelop
Dorian Parks
President
408 W Birch Avenue Belle Plaine, MN 56093
dorian@tidewaterhomesgroup.com
www.tidewaterhomesgroup.com
Licensed Realtor with Quiet Harbor Real Estate
Escape Gravity.
newell343 newell343
I am also interested in getting a design done for metal business cards. It would be cool to have them die cut, etched, and have our two color logo on them. Thanks.

```html
<!DOCTYPE html>
<html lang="en">
<head>
<meta charset="utf-8">
<title>Tidewater Homes Group – Business Card</title>
<link rel="stylesheet" href="https://fonts.googleapis.com/css2?family=Montserrat:wght@600;700&family=Open+Sans:wght@400;600&display=swap">
<style>
  :root {
    --bg: #8f9194;
    --card: #ffffff;
    --ink: #4a4d52;
    --muted: #6a6d72;
    --teal: #2fb3bd;
    --teal-light: #9fdde2;
    --orange: #d98a1f;
    --line: #b9bcc0;
  }
  * { margin: 0; padding: 0; box-sizing: border-box; }
  html, body { width: 1200px; height: 878px; overflow: hidden; }
  body {
    background: var(--bg);
    display: flex;
    align-items: center;
    justify-content: center;
    gap: 48px;
    font-family: "Open Sans", sans-serif;
    color: var(--ink);
  }
  .card {
    position: relative;
    width: 540px;
    height: 309px;
    background: var(--card);
    overflow: hidden;
    box-shadow: 0 6px 18px rgba(0,0,0,.18);
  }
  .brand {
    display: flex;
    align-items: center;
    gap: 12px;
  }
  .brand-dot {
    width: 34px; height: 34px;
    border-radius: 50%;
    background: var(--teal);
    flex: none;
  }
  .brand-name {
    font-family: "Montserrat", sans-serif;
    font-weight: 700;
    color: var(--ink);
    letter-spacing: .06em;
    text-transform: uppercase;
    line-height: 1.15;
  }
  /* front */
  .card-front { display: flex; align-items: center; justify-content: center; }
  .card-front .brand-name { font-size: 26px; }
  .card-front .brand-dot { width: 46px; height: 46px; }
  /* back */
  .card-back .brand { position: absolute; left: 30px; top: 34px; }
  .card-back .brand-name { font-size: 17px; }
  .contact-list {
    position: absolute; left: 30px; top: 108px;
    list-style: none;
    font-size: 12px; color: var(--muted);
  }
  .contact-list li { display: flex; align-items: center; gap: 8px; margin-bottom: 5px; }
  .contact-list svg { width: 11px; height: 11px; fill: var(--teal); flex: none; }
  .person { position: absolute; right: 40px; top: 104px; text-align: left; }
  .person-name {
    font-family: "Open Sans", sans-serif; font-weight: 600;
    font-size: 19px; color: var(--teal);
  }
  .person-title { font-size: 12px; color: var(--orange); margin-top: 2px; }
  .address {
    position: absolute; right: 40px; bottom: 34px;
    font-size: 12px; color: var(--muted); line-height: 1.45;
  }
  .swoosh { position: absolute; left: 0; bottom: 0; width: 540px; height: 120px; }
</style>
</head>
<body>
  <section class="card card-front">
    <div class="brand">
      <span class="brand-dot"></span>
      <span class="brand-name">Tidewater<br>Homes Group</span>
    </div>
  </section>

  <section class="card card-back">
    <div class="brand">
      <span class="brand-dot"></span>
      <span class="brand-name">Tidewater<br>Homes Group</span>
    </div>

    <ul class="contact-list">
      <li><svg viewBox="0 0 24 24"><path d="M6.6 10.8a15 15 0 0 0 6.6 6.6l2.2-2.2a1 1 0 0 1 1-.25 11.4 11.4 0 0 0 3.6.6 1 1 0 0 1 1 1V20a1 1 0 0 1-1 1A17 17 0 0 1 3 4a1 1 0 0 1 1-1h3.5a1 1 0 0 1 1 1c0 1.25.2 2.45.6 3.6a1 1 0 0 1-.25 1z"/></svg>555 014 7890</li>
      <li><svg viewBox="0 0 24 24"><rect x="3" y="6" width="18" height="14" rx="1"/><rect x="7" y="2" width="10" height="5"/></svg>555 014 7890</li>
      <li><svg viewBox="0 0 24 24"><path d="M2 5h20v14H2z M2 5l10 8 10-8" /></svg>dorian@tidewaterhomesgroup.com</li>
    </ul>

    <div class="person">
      <p class="person-name">Dorian Parks</p>
      <p class="person-title">President</p>
    </div>

    <p class="address">408 W Birch Avenue<br>Belle Plaine, MN 56093</p>

    <svg class="swoosh" viewBox="0 0 540 120" preserveAspectRatio="none" aria-hidden="true">
      <path d="M0 30 C 120 70, 300 110, 540 118 L540 120 L0 120 Z" fill="var(--teal-light)" opacity=".55"/>
      <path d="M0 42 C 130 80, 300 112, 540 120 L0 120 Z" fill="var(--teal)"/>
      <path d="M0 52 C 140 88, 300 114, 540 120 L0 120 Z" fill="var(--card)"/>
    </svg>
  </section>
</body>
</html>
```